Software company seeks new website design

We are a UK based company called Meridian Loft. We build software which helps other businesses to manage their accounts and company finances. All of our clients enjoy full telephone based support as well as access to our software. So, we like to think that we are combining the best accountancy software in the world with a friendly human touch.
We need our homepage completely redesigned. At the moment we have two products which we want to highlight. They are called 'Quick Ledgerly' (which you can view at www.quickledgerly.example) and Tally Brook.
*VERY IMPORTANT!* We would like the focus of the site to be on our latest new product - Tally Brook.
We have included a variety of files to help you out, including graphics and some text. Our target audience is medium and large UK based companies who are interested in finding a cost effective and intelligent accountancy solution.
The main call to action on the home page should be EITHER 'learn more', 'find out more' or 'arrange a free demonstration'. If you are unsure about what the text should say then you can use 'Lorem Ipsum'.
Site that we like include:
http://vantorisoft.example/
http://www.plumegrid.example/
Thank you for viewing. We promise to give constructive feedback to every person who submits a design. Thank you so much. Good luck to you!
IMPORTANT UPDATE: THE ARTWORK HIVE WEBSITE KEEPS LOGGING ME OUT WHEN I TRY TO ADD FEEDBACK. I HAVE CONTACTED TECHNICAL SUPPORT AND I'M WAITING FOR A RESOLUTION. I SHALL OFFER FEEDBACK TO EVERY ONE OF YOU AS SOON AS THE ARTWORK HIVE WEBSITE IS WORKING PROPERLY
ANOTHER IMPORTANT UPDATE: I SAID ABOVE THAT I'D LIKE THE FOCUS ON THE SITE TO BE ON THE PRODUCT 'TALLY BROOK' - NOT QUICK LEDGERLY. ONE PERSON HAS ALREADY WASTED TIME BY NOT FOLLOWING THAT INSTRUCTION. SO, ONCE AGAIN - PLEASE MAKE THE FOCUS OF THE SITE ON TALLY BROOK - NOT QUICK LEDGERLY. THANKS FOLKS. I APPRECIATE YOU BEING HERE.
Reason: Sorry folks, there was a problem with the system which prevented me from leaving any feedback. That problem has now been resolved, however, the guy who is making the final decision is away for a few days. Thank you for everything so far. There's some really great designs so far. Every design will be checked out and given a comment. You have my word.
Reason: Sorry folks, it's been an incredibly busy week and we haven't had time to check the designs out.

```html
<!DOCTYPE html>
<html lang="en">
<head>
<meta charset="utf-8">
<title>Meridian Loft — Tally Brook</title>
<link href="https://fonts.googleapis.com/css2?family=Figtree:wght@300;400;600;700;800&display=swap" rel="stylesheet">
<style>
:root{
  --ink:#333;
  --muted:#8a8a8a;
  --tab:#6c6c6c;
  --tab-line:#858585;
  --hero-top:#00c6dd;
  --hero-bottom:#1f8fc9;
  --brand:#0b4f8c;
  --accent:#2a8fcf;
  --orange:#f9ad2a;
  --orange-dark:#f39a12;
  --card-frame:#e6e6e6;
  --footer:#ebebeb;
  --white:#fff;
}
*{box-sizing:border-box;margin:0;padding:0}
html,body{width:1016px;height:1200px;overflow:hidden;background:var(--white)}
body{font-family:"Figtree",sans-serif;color:var(--ink)}
.page{position:relative;width:1016px;height:1200px;overflow:hidden}

.utility-bar{position:absolute;left:389px;top:0;width:584px;height:34px;background:var(--tab);border-radius:0 0 8px 8px;display:flex;align-items:center;white-space:nowrap}
.utility-bar .menu{color:var(--white);font-size:16px;padding:0 10px 0 20px;height:34px;display:flex;align-items:center;gap:9px;border-right:1px solid var(--tab-line);white-space:nowrap}
.utility-bar .menu::after{content:"";border:4px solid transparent;border-top:7px solid #ddd;border-bottom:0}
.search{margin-left:13px;width:150px;height:24px;background:var(--white);border-radius:12px;display:flex;align-items:center;padding-left:10px;gap:12px;color:#aaa;font-size:15px;white-space:nowrap}

.brand{position:absolute;left:55px;top:72px;display:flex;align-items:center;gap:8px;font-size:24px;font-weight:600;color:var(--brand);white-space:nowrap}
.brand .mark{width:22px;height:22px;background:var(--brand)}

.main-nav{position:absolute;top:85px;right:42px;display:flex;gap:19px;font-size:16.5px;font-weight:600;color:#444;white-space:nowrap}

.hero{position:absolute;left:0;top:136px;width:1016px;height:386px;background:linear-gradient(var(--hero-top),var(--hero-bottom))}
.hero .product-square{position:absolute;left:60px;top:64px;width:96px;height:92px;background:linear-gradient(160deg,#fff,#bfe3ef 55%,#2ab4d9)}
.hero h1{position:absolute;left:180px;top:56px;font-size:74px;font-weight:300;color:var(--white);letter-spacing:-1px;line-height:1;white-space:nowrap}
.hero h1 strong{font-weight:700}
.hero .tagline{position:absolute;left:182px;top:124px;font-size:29px;font-weight:300;color:var(--white);white-space:nowrap}
.hero .pitch{position:absolute;left:175px;top:259px;font-size:24px;font-weight:400;color:var(--white);line-height:30px;white-space:nowrap}

.mascot{position:absolute;left:752px;top:178px;width:190px;height:412px;border-radius:95px 95px 40px 40px;background:linear-gradient(rgba(255,255,255,0.35),rgba(230,230,230,0.55))}
.cta{position:absolute;left:724px;top:368px;width:250px;height:102px;background:linear-gradient(var(--orange),var(--orange-dark));border-radius:3px;color:var(--white);font-size:38px;font-weight:800;display:flex;align-items:center;justify-content:center;white-space:nowrap}

.slider-dots{position:absolute;left:500px;top:535px;display:flex;gap:17px}
.slider-dots span{width:20px;height:20px;border-radius:50%;background:#eee;border:1px solid #ccc}
.slider-dots span.active{background:#4a4a4a;border-color:#4a4a4a}

.intro{position:absolute;left:99px;top:614px;width:850px;font-size:24px;font-weight:300;color:var(--muted);line-height:30px;text-align:justify;text-align-last:center}

.news-card{position:absolute;top:770px;width:402px;height:129px;background:var(--card-frame);border:1px solid #bdbdbd;padding:9px 10px}
.news-card .inner{background:var(--white);height:108px;box-shadow:0 2px 2px #bbb;padding:5px 9px}
.news-card h3{font-size:20px;font-weight:400;color:var(--accent);white-space:nowrap}
.news-card p{font-size:12.5px;font-weight:300;color:#666;line-height:16.5px;margin-top:2px}
.news-card .more{display:block;text-align:right;font-size:13px;color:var(--orange-dark);margin-top:2px}

.site-footer{position:absolute;left:0;top:945px;width:1016px;height:255px;background:var(--footer);border-top:1px solid #ddd}
.footer-col{position:absolute;top:31px;white-space:nowrap}
.footer-col h4{font-size:20.5px;font-weight:400;color:#333;margin-bottom:8px}
.footer-col li{list-style:none;font-size:16.5px;font-weight:300;color:#333;line-height:20px}
.social{display:flex;gap:16px;margin-top:9px}
.social span{width:35px;height:35px;background:var(--accent);border-radius:3px}
.footer-note{position:absolute;left:0;width:1016px;top:182px;text-align:center;font-size:12.5px;font-weight:600;color:#999;line-height:17px}
.footer-note .dot{display:inline-block;width:13px;height:13px;border-radius:50%;background:#1aa6e0;vertical-align:-2px;margin:0 10px}
</style>
</head>
<body>
<div class="page">
  <nav class="utility-bar">
    <span class="menu">Login</span>
    <span class="menu">Support</span>
    <span class="menu">Contact</span>
    <span class="menu">United States</span>
    <span class="search">
      <svg width="14" height="14" viewBox="0 0 14 14"><circle cx="5.5" cy="5.5" r="4" fill="none" stroke="#444" stroke-width="2"/><line x1="8.5" y1="8.5" x2="13" y2="13" stroke="#444" stroke-width="2.5"/></svg>
      search here
    </span>
  </nav>

  <div class="brand"><span class="mark"></span>Meridian Loft</div>

  <nav class="main-nav">
    <span>Home</span><span>Enterprise Solutions</span><span>iQL</span><span>Partners</span><span>Case Studies</span><span>News Blog</span><span>Contact Us</span>
  </nav>

  <section class="hero">
    <div class="product-square"></div>
    <h1>Tally <strong>Brook</strong></h1>
    <p class="tagline">Unlock the potential of your ERP system</p>
    <p class="pitch">All the reports you need, when you need them<br>formatted to suit you at a fixed monthly price</p>
  </section>

  <div class="mascot" role="img" aria-label="Cartoon illustration of a friendly woman in glasses holding up a sign"></div>
  <div class="cta">LEARN MORE</div>

  <div class="slider-dots"><span class="active"></span><span></span></div>

  <p class="intro">Meridian Loft is a specialist software company providing innovative solutions to enterprises in the private and public sector. Using patented software we provide complete cost effective solutions that offer exceptional value for money</p>

  <article class="news-card" style="left:89px">
    <div class="inner">
      <h3>New Feature Introduced!</h3>
      <p>“ The new Tally Brook has been built and to be integrated with meridian loft for better solutions to customers in order to meet what they need ... ”</p>
      <span class="more">Read more</span>
    </div>
  </article>
  <article class="news-card" style="left:551px">
    <div class="inner">
      <h3>New Feature Introduced!</h3>
      <p>“ The new Tally Brook has been built and to be integrated with meridian loft for better solutions to customers in order to meet what they need ... ”</p>
      <span class="more">Read more</span>
    </div>
  </article>

  <footer class="site-footer">
    <div class="footer-col" style="left:80px"><h4>About us</h4><ul><li>Company Info</li><li>Privacy Policy</li><li>Contact us</li></ul></div>
    <div class="footer-col" style="left:258px"><h4>Our Solutions</h4><ul><li>Consumer Products</li><li>Financial services</li><li>Public Sector</li><li>Manufacturing</li></ul></div>
    <div class="footer-col" style="left:470px"><h4>Services</h4><ul><li>Partners</li><li>Company</li><li>Community</li><li>Data</li></ul></div>
    <div class="footer-col" style="left:630px"><h4>Social Media</h4><ul><li>Follow us on</li></ul><div class="social"><span></span><span></span><span></span></div></div>
    <div class="footer-col" style="left:821px"><h4>Contact us</h4><ul><li>Store Locator</li><li>Site Map</li><li>Contact Us</li></ul></div>
    <p class="footer-note">For any questions<span class="dot"></span>0800 555 01 47<br>Copyright © Meridian Loft 2012</p>
  </footer>
</div>
</body>
</html>
```